Business Card design for Property Developer

We need a business card design for a Melbourne based Property Developer called "Kestrelmoor Holdings Pty Ltd".

We subdivide land and onsell to builders etc.

We already have a company logo, which is attached. Also I have attached the layout requirements from the printer. We would like a 2-sided design with one side displaying our logo by itself and the other with the required info, such as name, address, tel no., email, abn etc. The card will need to be used by 4 members of staff so name and contact details should be interchangable.
Updates

If possible, can you please write "name' "job position" "phone" "email" "address" on the card but leave them so I can add the details at a later time. Thank you. Also I plan on printing with UV spot printing as a background on the card. Keep this is mind when designing.

Thanks again.

Hello designers, please do not include pics of houses, house plansĀ or construction machinery etc as we really do not like the way it looks. Thank you.

Target Market(s)

Real Estate Agents, Land Owners, Local Council Departments, Govt Bodies, other Developers etc.

Industry/Entity Type

Business

Requirements
Must have
• 2-sided design with one side displaying our logo by itself and the other with the required info, such as name, address, tel no., email, abn etc.

```html
<!DOCTYPE html>
<html lang="en">
<head>
<meta charset="utf-8">
<title>Kestrelmoor Holdings – Business Card</title>
<link rel="stylesheet" href="https://fonts.googleapis.com/css2?family=Arimo:wght@400;700&display=swap">
<style>
  :root {
    --card-bg: #ffffff;
    --band-grey: #f2f2f2;
    --brand-navy: #253a8a;
    --accent-blue: #1e93d8;
    --ink: #111111;
  }
  html, body {
    margin: 0;
    padding: 0;
    width: 1200px;
    height: 783px;
    overflow: hidden;
    background: var(--card-bg);
  }
  .business-card {
    display: block;
    width: 1200px;
    height: 783px;
    font-family: "Arimo", Arial, sans-serif;
  }
  .info-band { fill: var(--band-grey); }
  .brand-dot { fill: var(--brand-navy); }
  .brand-name { fill: var(--brand-navy); font-weight: 700; font-size: 30px; }
  .person-name { fill: var(--accent-blue); font-weight: 700; font-size: 34px; }
  .job-title { fill: var(--ink); font-size: 29px; }
  .contact-label { fill: var(--accent-blue); font-size: 28px; }
  .contact-value { fill: var(--ink); font-size: 28px; }
  .address-line { fill: var(--ink); font-size: 29px; }
</style>
</head>
<body>
<svg class="business-card" viewBox="0 0 1200 783" xmlns="http://www.w3.org/2000/svg">
  <rect width="1200" height="783" fill="var(--card-bg)"/>

  <g class="brand-lockup">
    <circle class="brand-dot" cx="150" cy="392" r="20"/>
    <text class="brand-name" x="186" y="403">Kestrelmoor Holdings</text>
  </g>

  <polygon class="info-band" points="472,511 1061,178 1122,291 517,637"/>
  <polygon class="info-band" points="539,672 994,413 1055,522 592,820 560,820"/>

  <g class="identity">
    <text class="person-name" transform="translate(605,405) rotate(-30)">PERSON NAME</text>
    <text class="job-title" transform="translate(870,260) rotate(-30)">Job Position</text>
  </g>

  <g class="contact">
    <text transform="translate(517,556) rotate(-30)"><tspan class="contact-label">Phone</tspan><tspan class="contact-value"> 000-000-0000</tspan></text>
    <text transform="translate(539,595) rotate(-30)"><tspan class="contact-label">Email</tspan><tspan class="contact-value"> asdf@KestrelmoorHoldings.com</tspan></text>
  </g>

  <g class="address">
    <text class="address-line" transform="translate(605,698) rotate(-30)">Suite 000, Street Name</text>
    <text class="address-line" transform="translate(628,734) rotate(-30)">City, Province, Pin-Code</text>
  </g>
</svg>
</body>
</html>
```